Concreting tools catalogue

I need a catalogue to provide current and potential customers with the item we hold and their prices. THIS WILL HAVE TO BE A FILE THAT I CAN EDIT AS I WILL BE ADDING INFORMATION AND PICTURES. I have provided an example of what I want in the files. Logo to be used is provided in files.

Will be 10 pages approximately excluding front cover and the back.

COVER PAGE:
Underneath VARDO put the words "Professional Concrete Equipment"
In the top right corner put "2021". Underneath 2021 put "concrete power equipment and accesories".

BACK PAGE:
Add contact details

The image with two pipes will be use for pages with accesories and will hold a minimum of 2 items.

The third image will be used to display items that we have variations of. A table will be needed at the bottom of the page to display the prices of different variations.

Target Market(s)

concreter workers, industrial

Colors
33b8a4
ffffff

Requirements
Must have
• Please send the catalogue with both white and light grey textured backgorund that looks like concrete. So i can decide on which colour. Please use the green specified in the colours section.

Put sample photos of any 36" power trowels you find on google images.

Select a font suitable for the title of each page and a font used for descriptions.

```html
<!DOCTYPE html>
<html lang="en">
<head>
<meta charset="utf-8">
<title>VARDO Catalogue 2021 – Cover Spread</title>
<link rel="stylesheet" href="https://fonts.googleapis.com/css2?family=Archivo:wdth,wght@100,400;125,400;125,700;125,800&display=swap">
<style>
  :root {
    --teal: #3cc3cf;
    --teal-deep: #2fb8c6;
    --white: #ffffff;
    --page-grey: #efefef;
    --ink: #333333;
    --ink-soft: #555555;
    --stage: #dcdcdc;
  }
  * { box-sizing: border-box; margin: 0; padding: 0; }
  html, body { width: 1200px; height: 840px; overflow: hidden; }
  body {
    background: var(--stage);
    font-family: "Archivo", Arial, sans-serif;
    display: flex;
    align-items: center;
    justify-content: center;
  }
  .spread {
    display: flex;
    width: 1080px;
    height: 760px;
    box-shadow: 0 12px 30px rgba(0,0,0,0.18);
  }
  .page { position: relative; width: 540px; height: 760px; overflow: hidden; }

  /* Back page */
  .back-page { background: var(--page-grey); }
  .photo-pipes {
    position: absolute; left: 170px; top: 0; width: 370px; height: 330px;
    background: linear-gradient(135deg, #f4f4f4 0%, #dedede 45%, #f7f7f7 70%, #d8d8d8 100%);
  }
  .fittings { position: absolute; left: 60px; top: 380px; display: flex; gap: 60px; }
  .fitting {
    width: 110px; height: 110px;
    background: radial-gradient(circle at 40% 40%, #f6f6f6 0%, #d6d6d6 100%);
  }
  .back-brand {
    position: absolute; left: 60px; top: 520px;
    font-weight: 800; font-stretch: 125%; font-size: 28px;
    letter-spacing: 2px; color: var(--teal);
  }
  .back-blurb {
    position: absolute; left: 60px; top: 630px; width: 160px;
    font-size: 11px; line-height: 1.3; color: var(--ink-soft);
  }
  .contact {
    position: absolute; right: 40px; bottom: 40px;
    list-style: none; font-size: 11px; line-height: 1.35; color: var(--ink-soft);
  }

  /* Cover page */
  .cover-page { background: linear-gradient(160deg, var(--teal) 0%, var(--teal-deep) 100%); color: var(--white); }
  .edition { position: absolute; right: 40px; top: 46px; text-align: right; }
  .edition-year {
    font-weight: 800; font-stretch: 125%; font-size: 34px; letter-spacing: 4px; line-height: 1;
  }
  .edition-subtitle { font-size: 13px; line-height: 1.25; margin-top: 6px; font-weight: 700; }
  .cover-brand {
    position: absolute; left: 40px; right: 30px; bottom: 112px;
    font-weight: 800; font-stretch: 125%; font-size: 100px; letter-spacing: 2px; line-height: 1;
    white-space: nowrap;
  }
  .cover-rule {
    position: absolute; left: 0; right: 0; bottom: 96px; height: 4px; background: var(--white);
  }
  .cover-tagline {
    position: absolute; left: 40px; bottom: 62px;
    font-weight: 700; font-stretch: 125%; font-size: 17px; letter-spacing: 1px; line-height: 1.2;
    white-space: nowrap;
  }
</style>
</head>
<body>
  <main class="spread">
    <section class="page back-page">
      <div class="photo-pipes" role="img" aria-label="Two white PVC pipes lying diagonally"></div>
      <div class="fittings">
        <div class="fitting" role="img" aria-label="White cross pipe fitting"></div>
        <div class="fitting" role="img" aria-label="White tee pipe fitting"></div>
        <div class="fitting" role="img" aria-label="White wye pipe fitting"></div>
      </div>
      <div class="back-brand">VARDO</div>
      <p class="back-blurb">Lorem Ipsum is simply dummy text of the printing and typesetting industry.</p>
      <ul class="contact">
        <li>T: 000 0000 0000</li>
        <li>E: info@vardo.com</li>
        <li>W: vardo-tools.com</li>
      </ul>
    </section>

    <section class="page cover-page">
      <div class="edition">
        <div class="edition-year">2021</div>
        <div class="edition-subtitle">concrete power equipment<br>and accesories</div>
      </div>
      <h1 class="cover-brand">VARDO</h1>
      <div class="cover-rule"></div>
      <p class="cover-tagline">PROFESSIONAL CONCRETE EQUIPMENT</p>
    </section>
  </main>
</body>
</html>
```